Sign for a retail store selling handmade gifts

We need a sign for the outside of a retail store that will sell handmade products (small gifts, clothing, home décor) from around the world. The products sold in the store will be bright and colorful, and so we want the sign to reflect that in its color palette. (One design idea we had was to show the store name as part of a colorful tapestry or hand-stitched rug. However, that is only one idea, and we would like to see other design concepts as well.)
“Petalbrook–Sunvale” is the name of the store. And we would also like to include a tag line that says, “Unique treasures – globally sourced, locally sold”.

Thank you for the designs we have received so far. We find that we prefer designs that are simple, have a light background with colorful elements on top, and convey that our products are made by hand from around the world.

```html
<!DOCTYPE html>
<html lang="en">
<head>
<meta charset="utf-8">
<title>Petalbrook–Sunvale Store Sign</title>
<link rel="stylesheet" href="https://fonts.googleapis.com/css2?family=Cinzel:wght@600;700&family=Open+Sans:wght@600&display=swap">
<style>
  :root {
    --backdrop: #8c8c8c;
    --room-cream: #fbf4e6;
    --room-sand: #f3e4c8;
    --rug-rose: #f2c1b8;
    --rug-teal: #b9ddd6;
    --rug-saffron: #f6d58a;
    --band-teal: #1f8a8a;
    --band-coral: #e4572e;
    --band-saffron: #f2a900;
    --band-plum: #8e3b76;
    --stitch: #ffffff;
    --nameplate-bg: #ffffff;
    --nameplate-ink: #2e5e66;
    --nameplate-accent: #c2452a;
    --tagline-ink: #6b2a5a;
    --contact-ink: #33302c;
  }
  * { margin: 0; padding: 0; box-sizing: border-box; }
  html, body {
    width: 1200px;
    height: 1200px;
    overflow: hidden;
    background: var(--backdrop);
  }
  .canvas {
    position: relative;
    width: 1200px;
    height: 1200px;
  }
  .sign {
    position: absolute;
    left: 187px;
    top: 187px;
    width: 826px;
    height: 826px;
    overflow: hidden;
    background: var(--room-cream);
  }
  .sign__scene {
    position: absolute;
    inset: 0;
    background:
      linear-gradient(180deg, rgba(251,244,230,0) 55%, rgba(246,213,138,0.55) 72%, rgba(242,193,184,0.6) 86%, rgba(185,221,214,0.7) 100%),
      linear-gradient(100deg, var(--room-sand) 0%, var(--room-cream) 45%, var(--room-sand) 100%);
  }
  .sign__band {
    position: absolute;
    left: 0;
    width: 100%;
    height: 25px;
  }
  .sign__band::after {
    content: "";
    position: absolute;
    left: 0;
    right: 0;
    top: 11px;
    border-top: 2px dashed var(--stitch);
    opacity: 0.85;
  }
  .sign__band--top {
    top: 23px;
    background: linear-gradient(90deg, var(--band-teal) 0 25%, var(--band-saffron) 25% 50%, var(--band-coral) 50% 75%, var(--band-plum) 75% 100%);
  }
  .sign__band--bottom {
    top: 781px;
    background: linear-gradient(90deg, var(--band-plum) 0 25%, var(--band-coral) 25% 50%, var(--band-saffron) 50% 75%, var(--band-teal) 75% 100%);
  }
  .nameplate {
    position: absolute;
    left: 88px;
    top: 98px;
    width: 670px;
    height: 179px;
    background: var(--nameplate-bg);
    font-family: "Cinzel", serif;
    font-weight: 600;
    text-align: center;
    box-shadow: 0 0 0 3px var(--band-teal);
  }
  .nameplate::before {
    content: "";
    position: absolute;
    inset: 8px;
    border: 2px dashed var(--band-saffron);
  }
  .nameplate__primary {
    display: block;
    margin-top: 22px;
    font-size: 84px;
    line-height: 1;
    color: var(--nameplate-ink);
  }
  .nameplate__secondary {
    display: block;
    margin-top: 12px;
    font-size: 36px;
    line-height: 1;
    letter-spacing: 14px;
    padding-left: 14px;
    color: var(--nameplate-accent);
  }
  .tagline {
    position: absolute;
    left: 0;
    top: 364px;
    width: 100%;
    text-align: center;
    color: var(--tagline-ink);
    font-family: "Cinzel", serif;
    font-weight: 700;
    font-size: 60px;
    line-height: 71px;
  }
  .contact {
    position: absolute;
    left: 0;
    top: 634px;
    width: 100%;
    text-align: center;
    color: var(--contact-ink);
    font-family: "Open Sans", sans-serif;
    font-weight: 600;
    font-size: 20px;
    line-height: 30px;
    list-style: none;
  }
</style>
</head>
<body>
  <main class="canvas">
    <section class="sign">
      <div class="sign__scene" role="img" aria-label="Bright room with an armchair, window and a colourful handwoven rug on the floor"></div>
      <div class="sign__band sign__band--top"></div>

      <div class="nameplate">
        <span class="nameplate__primary">PETALBROOK</span>
        <span class="nameplate__secondary">SUNVALE</span>
      </div>

      <p class="tagline">“UNIQUE TREASURES<br>GLOBALLY SOURCED<br>LOCALLY SOLD”</p>

      <ul class="contact">
        <li>Phone: (555) 214-0387</li>
        <li>Email: hello@petalbrook-sunvale.com</li>
        <li>Website: petalbrook-sunvale.com</li>
      </ul>

      <div class="sign__band sign__band--bottom"></div>
    </section>
  </main>
</body>
</html>
```